Plovenworks business card

We need a modern business card - With our 4 colors - See web: www.plovenworks.dk

I have attached logo and som old business Cards we have - Lets Make the new ones shine...:-) -

Industry/Entity Type

Business

Requirements
Must have
• the logo with plovnworks only,

```html
<!DOCTYPE html>
<html lang="da">
<head>
<meta charset="utf-8">
<title>Plovenworks business card</title>
<link href="https://fonts.googleapis.com/css2?family=Questrial&family=Source+Sans+3:wght@400;600&display=swap" rel="stylesheet">
<style>
  :root {
    --stage: #000000;
    --card-front: #ffffff;
    --card-back: #f7f7f7;
    --lime: #a2c63b;
    --magenta: #e6097f;
    --orange: #ee7d22;
    --purple: #72166f;
    --ink: #1e1e1e;
  }
  * { margin: 0; padding: 0; box-sizing: border-box; }
  html, body { width: 1200px; height: 900px; overflow: hidden; background: var(--stage); }
  .stage { position: relative; width: 1200px; height: 900px; }

  .card { position: absolute; overflow: hidden; font-family: "Source Sans 3", sans-serif; color: var(--ink); }
  .card--front { left: 116px; top: 275px; width: 477px; height: 294px; background: var(--card-front); border-radius: 0 60px 0 60px; }
  .card--back  { left: 622px; top: 276px; width: 477px; height: 293px; background: var(--card-back); border-radius: 60px 0 60px 0; }

  /* front */
  .brand { position: absolute; left: 20px; top: 110px; width: 213px; text-align: center; }
  .brand__name { font-family: "Questrial", sans-serif; font-size: 17px; letter-spacing: 2.4px; color: var(--ink); }
  .brand__rule { height: 3px; background: var(--lime); margin-top: 8px; }
  .brand__tagline { font-size: 13px; margin-top: 9px; color: #333; }
  .brand__dot { position: absolute; left: 90px; top: -78px; width: 36px; height: 36px; border-radius: 50%; background: var(--lime); }

  .person { position: absolute; right: 19px; top: 115px; text-align: right; }
  .person__name { font-size: 19px; font-weight: 600; color: var(--lime); line-height: 1; }
  .person__title { font-size: 12.5px; margin-top: 4px; }

  .contacts { position: absolute; right: 24px; top: 176px; list-style: none; }
  .contacts li { display: flex; justify-content: flex-end; align-items: center; gap: 6px; font-size: 13px; height: 19.5px; }
  .contacts svg { width: 13px; height: 13px; flex: none; }

  /* back */
  .back-brand { position: absolute; left: 0; right: 0; top: 40px; text-align: center; font-family: "Questrial", sans-serif; font-size: 22px; letter-spacing: 2px; color: var(--magenta); }
  .back-person { position: absolute; left: 141px; width: 194px; top: 117px; text-align: center; font-family: "Questrial", sans-serif; font-size: 12px; letter-spacing: 1.2px; }
  .back-person__rule { height: 2px; background: var(--magenta); margin: 4px 0 5px; }
  .stripe { position: absolute; left: 0; right: 0; height: 5px; }
  .stripe--magenta { top: 169px; background: var(--magenta); }
  .stripe--lime { top: 191px; background: var(--lime); }
  .stripe--orange { top: 252px; background: var(--orange); }
  .stripe--purple { top: 272px; background: var(--purple); border-radius: 3px; }
  .address { position: absolute; left: 0; right: 0; top: 209px; text-align: center; font-size: 13px; line-height: 17px; }
</style>
</head>
<body>
<main class="stage">
  <section class="card card--front">
    <div class="brand">
      <span class="brand__dot"></span>
      <p class="brand__name">plovnworks</p>
      <div class="brand__rule"></div>
      <p class="brand__tagline">Medier til unge</p>
    </div>
    <div class="person">
      <p class="person__name">Malte Nørgaard</p>
      <p class="person__title">Salgsdirektor</p>
    </div>
    <ul class="contacts">
      <li>+45 40 12 34 56
        <svg viewBox="0 0 13 13"><rect width="13" height="13" rx="1.5" fill="#a2c63b"/><path d="M3 8.5h7v1.5H3zM4 5c0-1.5 5-1.5 5 0v1H8V5.5c-1-.6-2-.6-3 0V6H4z" fill="#fff"/></svg></li>
      <li>mn@plovenworks.dk
        <svg viewBox="0 0 13 13"><rect width="13" height="13" rx="1.5" fill="#a2c63b"/><rect x="2.5" y="3.5" width="8" height="6" fill="#fff"/><path d="M2.5 3.5l4 3 4-3" stroke="#a2c63b" fill="none"/></svg></li>
      <li>www.plovenworks.dk
        <svg viewBox="0 0 13 13"><rect width="13" height="13" rx="1.5" fill="#c9de8e"/><path d="M4 9l5-5M3.5 7.5l-1 1a1.4 1.4 0 002 2l1-1M9.5 5.5l1-1a1.4 1.4 0 00-2-2l-1 1" stroke="#fff" stroke-width="1.2" fill="none"/></svg></li>
    </ul>
  </section>

  <section class="card card--back">
    <p class="back-brand">plovnworks</p>
    <div class="back-person">
      <p>Malte Nørgaard</p>
      <div class="back-person__rule"></div>
      <p>Salgsdirektør</p>
    </div>
    <div class="stripe stripe--magenta"></div>
    <div class="stripe stripe--lime"></div>
    <p class="address">Kastanievej 14 - 2000<br>Frederiksberg -Tlf. 38 12 40 77</p>
    <div class="stripe stripe--orange"></div>
    <div class="stripe stripe--purple"></div>
  </section>
</main>
</body>
</html>
```